Mesa Lumbre, Mexican Restaurant Menu

We need a menu design for a Mexican Restaurant in Dubai UAE

The concept of the Restaurant is as a Mexican Taqueria, That is simple street food like tacos, burritos, quesadillas, etc

We want a menu that is fun to read and that keeps a casual / street / urban feeling.If possible on a single page or 2 maximum so we can print on both sides and have it laminated

We are attaching photos of our logo and of the food that we will be serving, we are open to ideas and suggestions to try to make this as fun/casual as possible.

Also attaching photos of the style of tables we will use at the restaurant

Please avoid using tex mex items, like Crispy Taco Shells, Chiili, Cheddar Cheese , Fajitas, etc

Prices are not yet decided in the meantime you can use any price for the menu items.

If you can not include a photo for any single item on the menu, or you think it wouldn't look good, the ones that must be are.

1.-Tacos Al Pastor (this is the star of the show)
2-Guacamole
3-Burritos
4- Some Specials and alambres (photos attached)

Menu Items should have the description of ingredients on english and spanish (attached in menu file)

Any other idea or phrase trying to keep it fun and to show people that this is authentic mexican food and not tex mex would be nice to have.

If you have any doubts please contact us! Thanks for your help!

Target Market(s)

Expats living in Dubai + Latin Community,

Industry/Entity Type

Mexican Restaurant

Font styles to use
Other font styles liked:
• Helsinki, Helvetica , Klinic Slab

Colors
33a6d7
ec1f27
0455a3
fbee3d
9bcb3b
cadf82
f59195
85cae6
e34297

Requirements
Must have
• Fun to read, Preference on a Single page or 2 so we can print on both sides Or a Tri Fold so we can also use it for our Home Delivery Take away menu. Photos , Item ingredients in Spanish/English (attached on the menu file)
Nice to have
• Fun phrases, Reference to mexican food or characters
Should not have
• Tex Mex Items like Taco Shells , Chiili con Carne, Cheddar cheese

```html
<!DOCTYPE html>
<html lang="en">
<head>
<meta charset="utf-8">
<title>Mesa Lumbre — Menu</title>
<link rel="stylesheet" href="https://fonts.googleapis.com/css2?family=Bree+Serif&family=Kreon:wght@400&family=Merriweather:wght@400&family=Sriracha&family=Gochi+Hand&display=swap">
<style>
  :root {
    --paper: #f1f1ef;
    --paper-light: #ffffff;
    --red: #e2262d;
    --cyan: #33b4e6;
    --cyan-frame: #3bc1ee;
    --ink: #262626;
    --bubble-ink: #1b2a36;
    --guac-light: #a9c25a;
    --guac-dark: #7f9c3a;
  }
  * { margin: 0; padding: 0; box-sizing: border-box; }
  html, body { width: 1200px; height: 764px; overflow: hidden; background: var(--paper); }
  .menu {
    position: relative; width: 1200px; height: 764px; overflow: hidden;
    background: radial-gradient(circle at 60% 40%, #f6f6f4 0%, var(--paper) 70%);
    font-family: "Kreon", Georgia, serif;
  }
  .corner { position: absolute; left: 0; top: 0; }
  .brand { position: absolute; left: 22px; top: 48px; display: flex; align-items: center; gap: 8px; }
  .brand-mark { width: 14px; height: 14px; background: var(--red); }
  .brand-name { font-family: "Bree Serif", Georgia, serif; color: var(--red); font-size: 34px; line-height: 1; }
  .brand-tag { position: absolute; left: 44px; top: 90px; color: var(--red); font-family: "Merriweather", Georgia, serif; font-size: 9px; letter-spacing: 2px; }

  .section-title { position: absolute; color: var(--red); font-family: "Bree Serif", Georgia, serif; font-style: italic; font-weight: 400; font-size: 27px; line-height: 32px; white-space: nowrap; }
  .section-sub { font-family: "Sriracha", cursive; color: var(--cyan); font-style: normal; font-size: 17px; margin-left: 8px; }

  .name, .price { position: absolute; color: var(--red); font-family: "Kreon", Georgia, serif; font-weight: 400; font-size: 17px; line-height: 20px; white-space: nowrap; }
  .name .inline-en { font-family: "Sriracha", cursive; color: var(--cyan); font-size: 14px; margin-left: 4px; }
  .desc { position: absolute; color: var(--ink); font-family: "Merriweather", Georgia, serif; font-size: 11px; line-height: 16px; white-space: nowrap; }
  .en { position: absolute; color: var(--cyan); font-family: "Sriracha", cursive; font-size: 13px; line-height: 16px; white-space: nowrap; }

  .photo { position: absolute; background: var(--cyan-frame); padding: 6px 6px 0; box-shadow: 0 2px 6px rgba(0,0,0,.18); }
  .photo-fill { width: 100%; height: 100%; }
  .photo-caption { position: absolute; left: 0; right: 0; bottom: 0; text-align: center; color: #fff; font-family: "Gochi Hand", cursive; }

  .bubble { position: absolute; background: var(--cyan); border-radius: 50%; color: var(--bubble-ink); font-family: "Gochi Hand", cursive; text-align: center; display: flex; flex-direction: column; justify-content: center; }
  .bubble-tail { position: absolute; }
  .food-area { position: absolute; background: linear-gradient(160deg, var(--guac-light), var(--guac-dark)); }
</style>
</head>
<body>
<main class="menu">

  <svg class="corner" width="400" height="200" aria-hidden="true">
    <polygon points="0,0 392,0 0,192" fill="var(--paper-light)"/>
    <line x1="392" y1="0" x2="0" y2="192" stroke="#d2d2d0" stroke-width="1.5"/>
  </svg>
  <div class="brand"><span class="brand-mark"></span><span class="brand-name">Mesa Lumbre</span></div>
  <div class="brand-tag">URBAN MEXICAN FOOD</div>

  <!-- Appetizers -->
  <h2 class="section-title" style="left:104px; top:148px;">La Bonata<span class="section-sub">Appetizers</span></h2>

  <div class="name" style="left:27px; top:195px;">Rosa’s Famous Guacamole with Chips</div><div class="price" style="left:354px; top:195px;">$10</div>
  <div class="name" style="left:27px; top:221px;">Queso Fundido<span class="inline-en">Melted Cheese</span></div><div class="price" style="left:354px; top:221px;">$9</div>
  <div class="desc" style="left:43px; top:242px;">Plain or with Champinones/Mushrooms</div>

  <div class="name" style="left:27px; top:263px;">Nachos</div>
  <div class="name" style="left:54px; top:283px;">• De Pastor</div><div class="price" style="left:354px; top:283px;">$5</div>
  <div class="desc" style="left:82px; top:302px;">Tower of chips covered with cheese, beans,</div>
  <div class="desc" style="left:82px; top:318px;">jalapenos and our Famous Pastor</div>
  <div class="name" style="left:54px; top:336px;">• De Bistek</div><div class="price" style="left:354px; top:336px;">$5</div>
  <div class="desc" style="left:82px; top:354px;">Tower of chips covered with cheese, beans,</div>
  <div class="desc" style="left:82px; top:371px;">jalapenos and Delicious Steak</div>
  <div class="name" style="left:54px; top:390px;">• Tradicional</div><div class="price" style="left:354px; top:390px;">$5</div>
  <div class="desc" style="left:82px; top:411px;">Tower of chips covered with cheese, beans,</div>
  <div class="desc" style="left:82px; top:427px;">and jalapenos</div>

  <div class="name" style="left:27px; top:445px;">Sope</div><div class="price" style="left:354px; top:445px;">$4</div>
  <div class="desc" style="left:43px; top:468px;">Frijol, bistek o pollo</div>
  <div class="en" style="left:43px; top:487px;">Refried beans, steak, or chicken</div>
  <div class="name" style="left:27px; top:506px;">Quesadillas</div><div class="price" style="left:354px; top:506px;">$3</div>
  <div class="desc" style="left:43px; top:528px;">Tradicional, con Pollo o Veggie</div>
  <div class="en" style="left:43px; top:546px;">Plain, with chicken or veggie</div>

  <div class="photo" style="left:14px; top:572px; width:186px; height:186px; transform:rotate(-4deg);">
    <div class="photo-fill" role="img" aria-label="Photo of a Hawiana special plated on a restaurant table" style="height:150px; background:linear-gradient(135deg,#b98a5a,#e0b77a 45%,#c55a35 75%,#7e8a4a);"></div>
    <div class="photo-caption" style="font-size:22px; line-height:30px;">Hawiana</div>
  </div>

  <div class="food-area" role="img" aria-label="Photo of a bowl of fresh guacamole" style="left:212px; top:664px; width:144px; height:100px;"></div>

  <div class="bubble" style="left:246px; top:562px; width:154px; height:96px; transform:rotate(-6deg);">
    <span style="font-size:18px; line-height:22px;">How about some</span><span style="font-size:24px; line-height:28px;">Guacamole?!</span>
  </div>
  <svg class="bubble-tail" style="left:292px; top:650px;" width="20" height="16" aria-hidden="true"><polygon points="0,0 18,0 6,14" fill="var(--cyan)"/></svg>

  <!-- Tacos -->
  <h2 class="section-title" style="left:436px; top:46px;">Tacos</h2>
  <div class="bubble" style="left:536px; top:42px; width:86px; height:56px; transform:rotate(-8deg); font-size:13px; line-height:15px;">
    <span>The authentic</span><span>Mexican Taco!</span>
  </div>
  <svg class="bubble-tail" style="left:546px; top:88px;" width="16" height="14" aria-hidden="true"><polygon points="6,0 16,2 0,12" fill="var(--cyan)"/></svg>

  <div class="name" style="left:469px; top:88px;">Al Pastor</div><div class="price" style="left:713px; top:88px;">$6</div>
  <div class="name" style="left:469px; top:114px;">De Bistek(s) con Queso</div><div class="price" style="left:713px; top:114px;">$10</div>
  <div class="en" style="left:483px; top:134px;">Steak with cheese</div>
  <div class="name" style="left:469px; top:152px;">De Pollo</div><div class="price" style="left:713px; top:152px;">$12</div>
  <div class="en" style="left:483px; top:172px;">Chicken</div>
  <div class="name" style="left:469px; top:191px;">De Arrachera con Queso</div><div class="price" style="left:713px; top:191px;">$10</div>
  <div class="en" style="left:483px; top:212px;">Skirt Steak with cheese</div>
  <div class="name" style="left:469px; top:232px;">De Costilla’s</div><div class="price" style="left:713px; top:232px;">$8</div>
  <div class="en" style="left:483px; top:252px;">Beef Ribs Tacos</div>
  <div class="name" style="left:469px; top:271px;">De Cecina</div><div class="price" style="left:713px; top:271px;">$10</div>
  <div class="en" style="left:483px; top:291px;">Marinated Beef</div>
  <div class="name" style="left:469px; top:309px;">De Carne Asada</div><div class="price" style="left:713px; top:309px;">$7</div>
  <div class="en" style="left:483px; top:330px;">Grilled Beef</div>
  <div class="name" style="left:469px; top:351px;">Vegetariano con Queso</div><div class="price" style="left:713px; top:351px;">$11</div>
  <div class="en" style="left:483px; top:372px;">Veggie with cheese</div>

  <!-- Specials -->
  <h2 class="section-title" style="left:436px; top:417px;">Especials<span class="section-sub">Specials</span></h2>
  <div class="name" style="left:414px; top:464px;">Mula Terca</div><div class="price" style="left:762px; top:464px;">$6</div>
  <div class="desc" style="left:441px; top:487px;">Bistek, tocino, queso con tortilla de harina</div>
  <div class="en" style="left:441px; top:505px;">Steak, beef bacon, cheese with flour tortilla</div>
  <div class="name" style="left:414px; top:524px;">Hawiana</div><div class="price" style="left:762px; top:524px;">$10</div>
  <div class="desc" style="left:441px; top:548px;">Pollo, jamon, pina, tocino, queso con tortilla de harina</div>
  <div class="en" style="left:441px; top:568px;">Chicken, turkey ham, pineapple, beef bacon, cheese</div>
  <div class="en" style="left:441px; top:584px;">with flour tortilla</div>
  <div class="name" style="left:414px; top:602px;">Gringa</div><div class="price" style="left:762px; top:602px;">$12</div>
  <div class="desc" style="left:441px; top:626px;">Pastor,&nbsp; queso, cebolla, cilantro, pina con tortilla de harina</div>
  <div class="en" style="left:441px; top:646px;">Pastor, cheese, onion, cilantro, pineapple with flour</div>
  <div class="en" style="left:441px; top:662px;">tortilla</div>

  <!-- Burritos -->
  <h2 class="section-title" style="left:880px; top:48px;">Burritos</h2>
  <div class="name" style="left:811px; top:91px;">El Gringo Loco</div><div class="price" style="left:1157px; top:91px;">$6</div>
  <div class="desc" style="left:826px; top:113px;">Bistek, frijoles, lechuga, tomate, queso, guacamole y crema</div>
  <div class="en" style="left:826px; top:130px;">Steak, refried beas, lettuce, tomato, cheese, guacamole and</div>
  <div class="en" style="left:826px; top:147px;">cream</div>
  <div class="name" style="left:811px; top:164px;">El Chido</div><div class="price" style="left:1157px; top:164px;">$10</div>
  <div class="desc" style="left:826px; top:188px;">Pollo, frijoles, lechuga, tomate, queso, guacamole y crema</div>
  <div class="en" style="left:826px; top:206px;">Steak, refried beas, lettuce, tomato, cheese, guacamole and</div>
  <div class="en" style="left:826px; top:222px;">cream</div>
  <div class="name" style="left:811px; top:240px;">El Guapo</div><div class="price" style="left:1157px; top:240px;">$12</div>
  <div class="desc" style="left:826px; top:263px;">Arrachera, frijoles, queso, guacamole</div>
  <div class="en" style="left:823px; top:282px;">Skirt steak, refried beans, cheese, guacamole</div>
  <div class="name" style="left:811px; top:303px;">Super Burrito</div><div class="price" style="left:1157px; top:303px;">$6</div>
  <div class="desc" style="left:826px; top:326px;">Bistek o arrachera o pollo, tocino, frijoles</div>
  <div class="en" style="left:823px; top:344px;">Steak or skirt steak or chicken, beef bacon, refried beans</div>
  <div class="name" style="left:811px; top:363px;">Vegetariano</div><div class="price" style="left:1157px; top:363px;">$10</div>
  <div class="desc" style="left:826px; top:386px;">All the veggies with beans and cheese</div>

  <div class="photo" style="left:834px; top:420px; width:242px; height:190px; padding:6px; transform:rotate(-3deg);">
    <div class="photo-fill" role="img" aria-label="Photo of tacos with cilantro and onion" style="background:linear-gradient(135deg,#6b4a2e,#a8773f 40%,#5f7a34 70%,#3e2a1c);"></div>
  </div>
  <div class="photo" style="left:956px; top:444px; width:234px; height:214px; padding:6px; transform:rotate(8deg);">
    <div class="photo-fill" role="img" aria-label="Photo of pastor tacos with onion and lime" style="background:linear-gradient(135deg,#e7d9c2,#c4572c 45%,#e8c9a0 75%,#9fbf5a);"></div>
  </div>
  <div class="photo" style="left:896px; top:478px; width:184px; height:254px;">
    <div class="photo-fill" role="img" aria-label="Photo of a platter of tacos al pastor with salsa bowls" style="height:216px; background:linear-gradient(180deg,#6a5640,#8a6a48 40%,#b9763a 65%,#4a3a2a);"></div>
    <div class="photo-caption" style="font-size:22px; line-height:34px; letter-spacing:1px;">Tacos Al Pastor</div>
  </div>

</main>
</body>
</html>
```